2367 Halvorsen Avenue Medical Centre

We are looking for a design for new medical clinic.
We are accepting new patients at this new medical centre grand opening. Walk-ins are welcome.
Our cardiac and vascular surgical specialists are department heads at St Alder's Hospital, a leading teaching hospital in Toronto. These specialists will see cardiovascular consults are well as pre-surgical and post-surgical consultations and follow-ups.
Our lab is affiliated with several nuclear medicine clinics in the GTA.
Our Services Includes:
Family Practice
Cardiology Diagnostics
Cardiac & Vascular Surgical Consultation
Ultrasound & Vascular Testing
Open 6 days a week.
Ample Free Parking
Friendly Staffs

Target Market(s)

New Patients. Families of any age. Ethnic groups including Asians & Africans.

Industry/Entity Type

Medical

Font styles to use
Serif
Sans Serif
Decorative
Script
Other font styles liked:
• Arial calibri, verdana

Requirements
Must have
• Address:
• 2367 Halvorsen Avenue East
• Unit 225
• Scarborough, Ontario
• K7T 2P4
• Tel: (416) 555-0148
Nice to have
• Caring and inviting environment.
• Simple but classy.
• Standout colors.
Should not have
• Busy images. Aside from this, any ideas are welcome.

```html
<!DOCTYPE html>
<html lang="en">
<head>
<meta charset="utf-8">
<title>2367 Halvorsen Avenue Medical Centre – Grand Opening</title>
<link rel="stylesheet" href="https://fonts.googleapis.com/css2?family=Archivo+Black&family=Roboto+Condensed:ital,wght@0,400;0,700;0,900;1,900&family=Open+Sans:ital,wght@0,400;0,600;0,700;1,400&display=swap">
<style>
  :root {
    --red: #e0202a;
    --blue: #1a5fb4;
    --navy: #16386e;
    --yellow: #ffd21a;
    --white: #ffffff;
    --paper: #f4f8fc;
    --photo-light: #dfe9f2;
    --photo-mid: #b9cbdc;
    --photo-warm: #e7cdb9;
    --text: #1d2b44;
  }
  html, body { margin: 0; padding: 0; overflow: hidden; background: var(--white); }
  .flyer {
    position: relative;
    width: 857px; height: 1200px;
    overflow: hidden;
    background: var(--paper);
    font-family: "Open Sans", Arial, sans-serif;
    color: var(--text);
  }
  .hero-photo {
    position: absolute; left: 180px; top: 0; width: 677px; height: 880px;
    background:
      radial-gradient(ellipse at 40% 30%, var(--photo-warm) 0%, transparent 45%),
      radial-gradient(ellipse at 75% 70%, var(--photo-mid) 0%, transparent 55%),
      linear-gradient(90deg, var(--paper) 0%, var(--photo-light) 30%, var(--photo-mid) 100%);
  }
  .invite-ribbon { position: absolute; top: 0; right: 0; width: 200px; height: 200px; }
  .headline { position: absolute; left: 38px; top: 22px; }
  .headline .grand {
    font-family: "Archivo Black", Arial, sans-serif;
    color: var(--yellow);
    font-size: 54px; line-height: 56px;
    -webkit-text-stroke: 2px var(--red);
    text-transform: uppercase;
    margin: 0;
  }
  .headline .grand span { display: block; }
  .headline .grand .opening { padding-left: 70px; }
  .headline .new-clinic {
    margin: 26px 0 0 0;
    font-family: "Roboto Condensed", Arial, sans-serif;
    font-weight: 900;
    line-height: 42px;
  }
  .new-clinic .new { display: block; color: var(--red); font-size: 42px; padding-left: 10px; }
  .new-clinic .medical { display: block; color: var(--red); font-size: 42px; }
  .new-clinic .clinic { display: block; color: var(--blue); font-size: 46px; padding-left: 34px; }
  .walkin-badge {
    position: absolute; left: 14px; top: 318px; width: 420px; height: 420px;
    border-radius: 50%; background: var(--red);
    border: 8px solid var(--white); box-sizing: border-box;
    box-shadow: 0 6px 18px rgba(0,0,0,.18);
    display: flex; flex-direction: column; align-items: center; justify-content: center;
    font-family: "Roboto Condensed", Arial, sans-serif; font-weight: 900;
    color: var(--white); text-transform: uppercase; line-height: 1.02;
  }
  .walkin-badge span { display: block; font-size: 68px; }
  .walkin-badge .walkin { font-style: italic; font-size: 76px; }
  .open-badge {
    position: absolute; left: 243px; top: 210px; width: 188px; height: 188px;
    border-radius: 50%; background: var(--blue);
    border: 5px solid var(--white); box-sizing: border-box;
    display: flex; flex-direction: column; align-items: center; justify-content: center;
    font-family: "Roboto Condensed", Arial, sans-serif; font-weight: 900;
    color: var(--white); text-transform: uppercase; line-height: 1;
  }
  .open-badge .small { font-size: 30px; }
  .open-badge .big { font-size: 40px; color: var(--yellow); margin: 4px 0; }
  .booking { position: absolute; left: 114px; top: 748px; }
  .booking .call-label {
    margin: 0; font-family: "Roboto Condensed", Arial, sans-serif; font-weight: 700;
    font-size: 34px; line-height: 40px; color: var(--navy); text-transform: uppercase;
  }
  .booking .phone {
    margin: 0; font-family: "Roboto Condensed", Arial, sans-serif; font-weight: 700;
    font-size: 84px; line-height: 92px; color: var(--red);
  }
  .services { position: absolute; left: 114px; top: 912px; }
  .services h2 {
    margin: 0 0 8px; font-family: "Roboto Condensed", Arial, sans-serif; font-weight: 700;
    font-size: 26px; line-height: 32px; color: var(--navy); text-transform: uppercase;
  }
  .services ul { margin: 0; padding: 0; list-style: none; }
  .services li {
    font-size: 20px; line-height: 30px; font-weight: 600; color: var(--text);
    padding-left: 22px; position: relative;
  }
  .services li::before {
    content: ""; position: absolute; left: 4px; top: 11px;
    width: 9px; height: 9px; border-radius: 50%; background: var(--blue);
  }
  .address-bar {
    position: absolute; left: 0; bottom: 0; width: 100%; height: 40px;
    background: var(--red); color: var(--white);
    font-family: "Open Sans", Arial, sans-serif; font-size: 16px; font-weight: 700;
    display: flex; align-items: center; padding-left: 40px; box-sizing: border-box;
    text-transform: uppercase;
  }
  .address-bar em { font-style: italic; font-weight: 400; text-transform: none; margin-right: 8px; color: var(--yellow); }
</style>
</head>
<body>
<main class="flyer">
  <div class="hero-photo" role="img" aria-label="Smiling mother holding a baby beside a doctor with a stethoscope, and a digital blood pressure monitor in the foreground"></div>

  <svg class="invite-ribbon" viewBox="0 0 200 200">
    <polygon points="80,0 140,0 200,60 200,120" fill="var(--red)"/>
    <text x="0" y="0" transform="translate(148,56) rotate(45)" text-anchor="middle"
          font-family="Open Sans, Arial, sans-serif" font-style="italic" font-weight="700"
          font-size="19" fill="#ffffff">you are invited!</text>
  </svg>

  <header class="headline">
    <h1 class="grand"><span>Grand</span><span class="opening">Opening</span></h1>
    <p class="new-clinic"><span class="new">New</span><span class="medical">Medical</span><span class="clinic">CLINIC</span></p>
  </header>

  <div class="walkin-badge">
    <span>Accepting</span>
    <span class="walkin">Walk-In</span>
    <span>Patients</span>
  </div>

  <div class="open-badge">
    <span class="small">Open</span>
    <span class="big">6 Days</span>
    <span class="small">A Week</span>
  </div>

  <section class="booking">
    <p class="call-label">To book appointment please call</p>
    <p class="phone">(416) 555-0148</p>
  </section>

  <section class="services">
    <h2>Our services includes:</h2>
    <ul>
      <li>Family Practice</li>
      <li>Cardiology Diagnostics</li>
      <li>Cardiac &amp; Vascular Surgical Consultation</li>
      <li>Ultrasound &amp; Vascular Testing</li>
    </ul>
  </section>

  <footer class="address-bar">
    <em>visit the clinic at:</em> 2367 Halvorsen Avenue East, Unit 225, Scarborough, Ontario, K7T 2P4
  </footer>
</main>
</body>
</html>
```